'Bright Ledger Hidden Keys' Book Cover

I need a professional book cover design for my new upcoming book that shows people how to get a high credit score.

Here are my two websites:

https://www.moneywordbank-lexa.info
https://moneywordbank-lexa.com/

I am looking for a clean, professional design that pops (emotional touch) and separates from the other books that are on the market. Cover aspect ratio 1:4 for Pagewisp version and 1:5 for the paperback version. Yellow or blue are good colors - but not must. See the basic examples that I provided. File delivery format PDF.

Book Title: Bright Ledger Hidden Keys
Byline: The Quick Lift And Mend Manual for Stellar Borrowing

Currently on Brindlecart pre-order:
https://www.brindlecart.example/Bright-Ledger-Hidden-Keys-Stellar-ebook/dp/Q48MPLRT71

I am the author of 36 published books on Brindlecart. My author profile is here:
brindlecart.example/author/gideonvarly

Targeted audience: People that want to improve or repair their bad credit score.

Target Market(s)

People/consumers in the US that want to improve or repair their credit score.

Industry/Entity Type

Consumer

Font styles to use
Sans Serif

Colors

Designer to choose colors to be used in the design.

Requirements
Must have
• Author name, Title, byline, and graphic element(s).
Nice to have
• - 2020 edition logo / batch

```html
<!DOCTYPE html>
<html lang="en">
<head>
<meta charset="utf-8">
<title>Bright Ledger Hidden Keys – Book Cover</title>
<link rel="stylesheet" href="https://fonts.googleapis.com/css2?family=Oswald:wght@500;600;700&display=swap">
<style>
  :root {
    --page-bg: #ffffff;
    --cover-blue-top: #1f6aa6;
    --cover-blue-bottom: #14508a;
    --title-yellow: #f7e51b;
    --title-blue: #2ba4e2;
    --program-white: #ffffff;
    --glow-light: #5fc4f0;
    --card-light: #eaf8fc;
    --card-mid: #a6dcef;
  }
  * { margin: 0; padding: 0; box-sizing: border-box; }
  html, body {
    width: 1200px;
    height: 726px;
    overflow: hidden;
    background: var(--page-bg);
  }
  .stage {
    position: relative;
    width: 1200px;
    height: 726px;
    display: flex;
    align-items: center;
    justify-content: center;
  }
  .book-cover {
    display: block;
    width: 474px;
    height: 690px;
    box-shadow: 0 6px 18px rgba(0, 0, 0, 0.18);
  }
  .cover-type {
    font-family: 'Oswald', 'Arial Narrow', sans-serif;
    text-transform: uppercase;
  }
  .title-top { font-weight: 700; font-size: 118px; fill: var(--title-yellow); }
  .title-bottom { font-weight: 600; font-size: 95px; fill: var(--title-blue); }
  .byline-yellow { font-weight: 600; font-size: 29px; fill: var(--title-yellow); }
  .byline-blue { font-weight: 600; font-size: 40px; fill: var(--title-blue); }
  .author-name { font-weight: 700; font-size: 95px; fill: var(--title-yellow); }
  .program-name {
    font-family: 'Oswald', 'Arial Narrow', sans-serif;
    font-weight: 500;
    font-size: 22px;
    fill: var(--program-white);
  }
</style>
</head>
<body>
<main class="stage">
  <svg class="book-cover" viewBox="0 0 474 690" xmlns="http://www.w3.org/2000/svg" aria-labelledby="cover-title">
    <title id="cover-title">Bright Ledger Hidden Keys by Gideon Varly</title>
    <defs>
      <linearGradient id="cover-bg" x1="0" y1="0" x2="0" y2="1">
        <stop offset="0" stop-color="var(--cover-blue-top)"/>
        <stop offset="1" stop-color="var(--cover-blue-bottom)"/>
      </linearGradient>
      <radialGradient id="hand-glow" cx="0.35" cy="0.7" r="0.6">
        <stop offset="0" stop-color="var(--glow-light)" stop-opacity="0.75"/>
        <stop offset="1" stop-color="var(--glow-light)" stop-opacity="0"/>
      </radialGradient>
      <linearGradient id="card-fill" x1="0" y1="0" x2="1" y2="1">
        <stop offset="0" stop-color="var(--card-mid)"/>
        <stop offset="0.5" stop-color="var(--card-light)"/>
        <stop offset="1" stop-color="var(--card-light)"/>
      </linearGradient>
    </defs>

    <rect class="cover-background" width="474" height="690" fill="url(#cover-bg)"/>

    <g class="cover-photo" role="img" aria-label="Photo of a hand holding up a white credit card in blue light">
      <ellipse cx="190" cy="480" rx="190" ry="150" fill="url(#hand-glow)"/>
      <path d="M150 361 L371 195 Q378 190 381 198 L446 404 Q449 412 441 416 L206 553 Q198 557 195 549 L146 372 Q144 365 150 361 Z" fill="url(#card-fill)"/>
    </g>

    <g class="cover-type">
      <text class="title-top" x="15" y="109" textLength="432" lengthAdjust="spacingAndGlyphs">Bright Ledger</text>
      <text class="title-bottom" x="17" y="192" textLength="428" lengthAdjust="spacingAndGlyphs">Hidden Keys</text>

      <text class="byline-yellow" x="15" y="247" textLength="190" lengthAdjust="spacingAndGlyphs">The Quick Lift And</text>
      <text class="byline-blue" x="15" y="283" textLength="163" lengthAdjust="spacingAndGlyphs">Mend Manual</text>
      <text class="byline-yellow" x="15" y="315" textLength="196" lengthAdjust="spacingAndGlyphs">For Stellar Borrowing</text>

      <text class="author-name" x="15" y="632" textLength="440" lengthAdjust="spacingAndGlyphs">Gideon Varly</text>
    </g>
    <text class="program-name" x="237" y="670" text-anchor="middle" textLength="309" lengthAdjust="spacingAndGlyphs">Varly Financial Literacy Program</text>
  </svg>
</main>
</body>
</html>
```